District Manager Business Card

Hello, I own 3 automotive repair shops that are all 3 different names. I need a card that has all 3 locations and logos on it. Just a simple, modern, clean design. I selected double sided, but If a single side is more ideal, thats ok too. I am open to explore both options. I attached the 3 logos in a few different formats.

Industry/Entity Type

Auto Repair

Contact Information for Business Card

Requirements
Must have
• Location information:
Q&L Automotive
482 Birchfield Ave.
Hollisford TN 00101

MOTO MEND
257 Pine Hollow Turnpike
Ashgrove TN 00102

Brantmoor Tire & Auto
614 North Aspen Ave.
Wrenfield TN 00103

District Manager - Dale Hobart - Dale@qandlauto-example.com - Cell: 555-555-0196
Nice to have
• This can be a single or a double sided card. Just want a clean card that shows all 3 locations.

```html
<!DOCTYPE html>
<html lang="en">
<head>
<meta charset="utf-8">
<title>Dale Hobart – District Manager Business Card</title>
<link rel="stylesheet" href="https://fonts.googleapis.com/css2?family=Roboto:wght@300;400;500;700&display=swap">
<style>
  :root {
    --page: #e6e6e6;
    --card-dark: #1c1c1d;
    --card-light: #f7f7f7;
    --ink-light: #f2f2f2;
    --ink-dark: #111111;
    --rule-dark: #555555;
    --brand-blue: #22237a;
    --brand-red: #d42a2a;
  }
  * { margin: 0; padding: 0; box-sizing: border-box; }
  html, body {
    width: 1200px; height: 800px; overflow: hidden;
    background: var(--page);
    font-family: "Roboto", Arial, sans-serif;
  }
  .sheet {
    width: 1200px; height: 800px;
    display: flex; flex-direction: column; align-items: center; justify-content: center;
    gap: 40px;
  }
  .card {
    position: relative;
    width: 600px; height: 343px;
    box-shadow: 0 6px 18px rgba(0,0,0,0.18);
  }

  /* Front */
  .card-front { background: var(--card-dark); color: var(--ink-light); }
  .identity {
    position: absolute; left: 0; right: 0; top: 122px;
    text-align: center;
  }
  .identity-name {
    font-weight: 400; font-size: 34px; letter-spacing: 0.26em;
    padding-left: 0.26em;
  }
  .identity-title {
    font-weight: 400; font-size: 13px; letter-spacing: 0.04em;
    margin-top: 2px; padding-left: 60px;
  }
  .contact-row {
    position: absolute; left: 0; right: 0; bottom: 58px;
    display: flex; align-items: center; gap: 14px;
    font-size: 13px; font-weight: 400; letter-spacing: 0.04em;
    line-height: 1;
  }
  .contact-rule { height: 2px; background: var(--ink-light); }
  .contact-rule-long { flex: 1; }
  .contact-rule-short { width: 44px; }
  .contact-phone { margin-left: 8px; }

  /* Back */
  .card-back { background: var(--card-light); color: var(--ink-dark); }
  .brand-row {
    position: absolute; top: 34px; right: 34px;
    display: flex; align-items: center; gap: 22px;
  }
  .brand-name {
    display: flex; align-items: center; gap: 6px;
    font-size: 13px; font-weight: 700; letter-spacing: 0.03em; color: var(--brand-blue);
  }
  .brand-name-red { color: var(--brand-red); }
  .brand-name-black { color: var(--ink-dark); }
  .brand-dot { width: 14px; height: 14px; border-radius: 50%; background: var(--ink-dark); }
  .location-row {
    position: absolute; left: 40px; right: 40px; bottom: 34px;
    display: flex; justify-content: space-between; align-items: stretch;
  }
  .location {
    flex: 1; text-align: center;
    font-size: 14px; line-height: 1.2; font-weight: 400; font-style: normal;
  }
  .location-divider { width: 1px; background: var(--rule-dark); }
</style>
</head>
<body>
  <main class="sheet">
    <section class="card card-front" aria-label="Card front">
      <div class="identity">
        <h1 class="identity-name">DALE HOBART</h1>
        <p class="identity-title">DISTRICT MANAGER</p>
      </div>
      <div class="contact-row">
        <span class="contact-rule contact-rule-long"></span>
        <span class="contact-email">E : Dale@qandlauto-example.com</span>
        <span class="contact-phone">P : 555-555-0196</span>
        <span class="contact-rule contact-rule-short"></span>
      </div>
    </section>

    <section class="card card-back" aria-label="Card back">
      <div class="brand-row">
        <span class="brand-name">Q&amp;L AUTOMOTIVE</span>
        <span class="brand-name brand-name-red">MOTO MEND</span>
        <span class="brand-name brand-name-black"><span class="brand-dot"></span>BRANTMOOR</span>
      </div>
      <div class="location-row">
        <address class="location">Q&amp;L Automotive<br>482 Birchfield Ave.<br>Hollisford TN 00101</address>
        <span class="location-divider"></span>
        <address class="location">MOTO MEND<br>257 Pine Hollow Turnpike<br>Ashgrove TN 00102</address>
        <span class="location-divider"></span>
        <address class="location">Brantmoor Tire &amp; Auto<br>614 North Aspen Ave.<br>Wrenfield TN 00103</address>
      </div>
    </section>
  </main>
</body>
</html>
```